Packaging Design Project for Coffee Products

Velvet Roast is a new start-up specialising in Kopi Luwak (dubbed the most expensive coffee in the world). Due to the nature of our product, we would like to provide the premium experience and the first impression often begins with the packaging.

Our target audience is HNWs (high net-worth individuals), coffee connoisseurs, premium restaurants, cafes, and hotels. They are price insensitive and place high importance on quality and service.

We seek to have the packaging design and graphics that is artistic, clean, simple but sophisticated – representing our luxury product and premium service.

We have already thought about the packaging designs but need help when it comes to graphics and placements of information etc. Basically the packaging will consist of inner (aluminium vacuum sealed coffee pouch) and outer (paper tube) packagings.

For our detailed design specification and our logo (in EPS), please download attached files.
Updates

A number of you asked what type of font is used in the logo. The name is Philosopher. 

Project Deadline Extended
Reason: We are extending deadline by a week because we are close but not there yet. Hopefully this time extension will allow designers to tweak further their designs and submit new designs. Thanks for your understanding and cooperation. Regards VelvetRoast.

Target Market(s)

HNWs (high net-worth individuals), coffee connoisseurs, premium restaurants, cafes, and hotels. They are price insensitive and place high importance o

Industry/Entity Type

Product

Requirements
Must have
• -design must be scalable as we are not yet 100% fixed on dimensions, we have provided initial reference
-please refer to our design brief for details
Should not have
• -colourful splashes
-extremely big fonts and complicated designs
-

```html
<!DOCTYPE html>
<html lang="en">
<head>
<meta charset="utf-8">
<title>Velvet Roast – Kopi Luwak Pack</title>
<link href="https://fonts.googleapis.com/css2?family=Jost:wght@200&family=Questrial&display=swap" rel="stylesheet">
<style>
  :root {
    --page: #ffffff;
    --pack: #36302c;
    --tile: #231f1f;
    --rule: #4b4541;
    --accent: #d8d41a;
    --title: #e6e6e6;
  }
  html, body {
    margin: 0;
    padding: 0;
    width: 1200px;
    height: 2240px;
    overflow: hidden;
    background: var(--page);
  }
  .pack {
    position: absolute;
    left: 178px;
    top: 172px;
    width: 859px;
    height: 1890px;
    background: var(--pack);
    box-shadow: 6px 8px 14px rgba(0,0,0,0.35);
    font-family: "Questrial", "Century Gothic", sans-serif;
    color: var(--accent);
    overflow: hidden;
  }
  .brand-name {
    position: absolute;
    left: 60px;
    top: 126px;
    font-size: 34px;
    line-height: 1;
    letter-spacing: 0.5px;
    margin: 0;
  }
  .tagline {
    position: absolute;
    left: 66px;
    top: 356px;
    font-size: 32px;
    line-height: 1;
    margin: 0;
  }
  .divider {
    position: absolute;
    left: 0;
    top: 465px;
    width: 100%;
    height: 3px;
    background: var(--rule);
  }
  .tile {
    position: absolute;
    width: 97px;
    height: 97px;
    background: var(--tile);
  }
  .authentic-band {
    position: absolute;
    left: 296px;
    top: 1444px;
    width: 488px;
    height: 100px;
    background: var(--tile);
    display: flex;
    align-items: center;
    justify-content: center;
    font-size: 35px;
    margin: 0;
  }
  .product-title {
    position: absolute;
    left: 0;
    top: 0;
    width: 859px;
    height: 1890px;
  }
  .product-title text {
    font-family: "Jost", "Century Gothic", sans-serif;
    font-weight: 200;
    font-size: 138px;
    fill: var(--title);
  }
  .weight {
    position: absolute;
    left: 66px;
    top: 1792px;
    font-size: 28px;
    letter-spacing: 1px;
    line-height: 1;
    margin: 0;
  }
</style>
</head>
<body>
  <section class="pack">
    <p class="brand-name">VelvetRoast</p>
    <p class="tagline">a Premium Gourmet Coffee experience</p>
    <div class="divider"></div>

    <svg class="product-title" viewBox="0 0 859 1890" aria-label="Kopi Luwak">
      <text x="233" y="1712" textLength="1134" lengthAdjust="spacingAndGlyphs" transform="rotate(-90 233 1712)">KOPI LUWAK</text>
    </svg>

    <!-- column 4 -->
    <div class="tile" style="left:686px;top:72px"></div>
    <div class="tile" style="left:686px;top:210px"></div>
    <div class="tile" style="left:686px;top:347px"></div>
    <div class="tile" style="left:686px;top:486px"></div>
    <div class="tile" style="left:686px;top:625px"></div>
    <div class="tile" style="left:686px;top:760px"></div>
    <div class="tile" style="left:686px;top:895px"></div>
    <div class="tile" style="left:686px;top:1032px"></div>
    <div class="tile" style="left:686px;top:1171px"></div>
    <div class="tile" style="left:686px;top:1309px"></div>
    <div class="tile" style="left:686px;top:1585px"></div>
    <div class="tile" style="left:686px;top:1722px"></div>

    <!-- column 3 -->
    <div class="tile" style="left:557px;top:486px"></div>
    <div class="tile" style="left:557px;top:625px"></div>
    <div class="tile" style="left:557px;top:760px"></div>
    <div class="tile" style="left:557px;top:895px"></div>
    <div class="tile" style="left:557px;top:1032px"></div>
    <div class="tile" style="left:557px;top:1171px"></div>
    <div class="tile" style="left:557px;top:1309px"></div>
    <div class="tile" style="left:557px;top:1585px"></div>
    <div class="tile" style="left:557px;top:1722px"></div>

    <!-- column 2 -->
    <div class="tile" style="left:427px;top:1032px"></div>
    <div class="tile" style="left:427px;top:1171px"></div>
    <div class="tile" style="left:427px;top:1309px"></div>
    <div class="tile" style="left:427px;top:1585px"></div>
    <div class="tile" style="left:427px;top:1722px"></div>

    <!-- column 1 -->
    <div class="tile" style="left:297px;top:1585px"></div>
    <div class="tile" style="left:297px;top:1722px"></div>

    <p class="authentic-band">100% authentic Kopi Luwak</p>

    <p class="weight">200 grams</p>
  </section>
</body>
</html>
```